New Website Design for High Quality Sailing School

This client has revised it's logo and branding and wants to create a new website that delivers a high-quality compelling design. Please read the brief, wireframes, brand guidelines and logos really carefully before you start your design work.
Note that the winning designer, based on the homepage, will be expected to do the other internal page designs as a part of this project.

Target Market(s)

Mainly Young Adults (20-35), High Net Worth, Love Sailing and Adventures

Industry/Entity Type

Leisure

Number of Pages Required

5+ page

Font styles to use
Sans Serif
Other font styles liked:
• Hyperspace Race

Requirements
Must have
• Attention to detail, high quality designs, applying the new branding carefully, and clean as per the brief.
Nice to have
• Keep it simple, but use the imagery. Take a look at the sites they like.
Should not have
• Inconsistency in design theme

```html
<!DOCTYPE html>
<html lang="en">
<head>
<meta charset="utf-8">
<title>Meridian Sailing – Home</title>
<link href="https://fonts.googleapis.com/css2?family=Rajdhani:wght@400;500;600;700&family=Montserrat:wght@400;500;600;700&display=swap" rel="stylesheet">
<style>
:root{
  --red:#e8351f;
  --ink:#2b2b2b;
  --muted:#7a7a7a;
  --panel:#f5f4f2;
  --footer:#414141;
  --page:#eeeeee;
  --white:#ffffff;
}
*{box-sizing:border-box;margin:0;padding:0}
html,body{width:1200px;height:4644px;overflow:hidden;background:var(--page)}
body{font-family:'Montserrat',sans-serif;color:var(--ink)}
.site{position:absolute;left:150px;top:412px;width:900px;height:3820px;background:var(--white)}
.abs{position:absolute}
.display{font-family:'Rajdhani',sans-serif;font-weight:500;letter-spacing:1px;text-transform:uppercase}

/* header */
.brand{left:148px;top:30px;display:flex;align-items:center;gap:10px}
.brand-mark{width:26px;height:26px;background:var(--red)}
.brand-name{font-family:'Rajdhani',sans-serif;font-weight:700;font-size:17px;line-height:15px;letter-spacing:2px;color:var(--ink)}
.brand-name small{display:block;font-size:9px;letter-spacing:4px}
.top-links{left:500px;top:50px;display:flex;gap:16px;font-size:8px;color:var(--muted)}
.btn{display:inline-block;background:var(--red);color:#fff;font-size:7px;font-weight:600;letter-spacing:.8px;text-transform:uppercase;text-align:center}
.btn-header{left:673px;top:45px;width:76px;height:20px;line-height:20px}
.main-nav{top:80px;left:389px;display:flex;gap:30px;font-size:7.5px;font-weight:600;letter-spacing:.6px;text-transform:uppercase}

/* photo fills */
.photo{position:absolute;overflow:hidden}
.hero{left:0;top:99px;width:900px;height:374px;background:
  radial-gradient(ellipse 60% 40% at 75% 78%,rgba(230,230,228,.55),transparent 70%),
  radial-gradient(ellipse 45% 35% at 30% 80%,rgba(120,70,50,.55),transparent 70%),
  linear-gradient(180deg,#8fa3b8 0%,#a9b8c6 30%,#7f8f9c 48%,#6a625c 62%,#3d3835 100%)}
.hero h1{position:absolute;top:150px;width:100%;text-align:center;color:#fff;font-size:25px;font-weight:400}
.hero .btn-dark{position:absolute;left:414px;top:196px;width:72px;height:16px;line-height:16px;background:#3b3b3b;border-radius:3px;font-size:6.5px}
.hero .learn{position:absolute;top:305px;width:100%;text-align:center;color:#fff;font-size:7px;font-weight:600;letter-spacing:.8px}
.stakes{left:0;top:473px;width:900px;height:374px;background:
  radial-gradient(ellipse 18% 55% at 60% 55%,rgba(214,170,130,.7),transparent 70%),
  radial-gradient(ellipse 40% 30% at 30% 90%,rgba(255,240,220,.8),transparent 70%),
  linear-gradient(180deg,#eceae6 0%,#f2e8da 55%,#c9a27c 82%,#6f6152 100%)}
.stakes h2{position:absolute;left:150px;top:46px;font-size:24px;font-weight:400;color:var(--ink)}
.stakes p{position:absolute;left:150px;top:102px;font-family:'Rajdhani',sans-serif;font-size:19px;line-height:27px;letter-spacing:.6px;text-transform:uppercase;color:var(--ink)}

.section-title{width:100%;text-align:center;font-size:25px;font-weight:400;line-height:34px}

/* cards */
.card{top:936px;width:188px;height:256px;display:flex;align-items:flex-end;justify-content:center;padding:0 14px 20px;text-align:center;color:#fff;font-size:9px;line-height:13px}
.card-1{left:149px;background:radial-gradient(ellipse 70% 40% at 50% 40%,rgba(230,210,190,.6),transparent 70%),linear-gradient(180deg,#b9a48c,#6f5f52)}
.card-2{left:356px;background:radial-gradient(ellipse 60% 40% at 50% 45%,rgba(220,220,220,.5),transparent 70%),linear-gradient(180deg,#9ab3c4,#2f5f78)}
.card-3{left:562px;background:linear-gradient(180deg,#8eb6d3 0%,#b08460 40%,#8a6448 55%,#2d6a8a 80%)}

/* feature tiles */
.tile{display:flex;flex-direction:column;justify-content:flex-end;color:#fff;padding:0 0 42px}
.tile h3{font-family:'Rajdhani',sans-serif;font-weight:500;font-size:17px;letter-spacing:.8px;text-transform:uppercase;line-height:20px;margin-bottom:12px}
.tile p{font-size:9.5px;line-height:13px;max-width:260px}
.tile-alumni{left:0;top:1316px;width:441px;height:281px;padding-left:149px;background:radial-gradient(ellipse 50% 40% at 60% 30%,rgba(210,160,110,.6),transparent 70%),linear-gradient(200deg,#5d8db3,#8a7264 60%,#3f4c57)}
.tile-instructors{left:459px;top:1316px;width:441px;height:281px;padding-left:23px;background:radial-gradient(ellipse 20% 40% at 75% 45%,rgba(230,230,235,.5),transparent 70%),linear-gradient(180deg,#7e8c98,#4f5d6a 45%,#2c3946)}
.tile-reviews{left:0;top:1616px;width:900px;height:279px;padding-left:149px;background:radial-gradient(ellipse 35% 30% at 55% 60%,rgba(150,200,170,.7),transparent 70%),linear-gradient(160deg,#2f4a24,#5e7e3a 45%,#79a86a 65%,#2e4a2a)}
.tile-certified{left:0;top:1915px;width:441px;height:281px;padding-left:149px;background:radial-gradient(ellipse 40% 25% at 70% 20%,rgba(90,110,60,.7),transparent 70%),linear-gradient(180deg,#1e4a6a,#2f6a7a 55%,#1b3b52)}
.tile-charter{left:459px;top:1915px;width:441px;height:281px;padding-left:23px;background:radial-gradient(ellipse 35% 45% at 45% 30%,rgba(235,235,240,.55),transparent 70%),linear-gradient(180deg,#7d98b4,#4a6784 60%,#2a3e55)}
.review-icons{display:flex;gap:4px;margin-top:12px}
.review-icons span{width:22px;height:22px;border:1.5px solid #fff;border-radius:50%}

/* press */
.press{top:2284px;left:149px;display:flex;gap:9px}
.press span{width:113px;height:69px;border:1px solid #e2e2e2;display:flex;align-items:center;justify-content:center;font-family:'Montserrat',sans-serif;font-weight:600;font-size:11px;color:var(--ink);text-align:center;line-height:13px}

/* how it works */
.how{left:0;top:2401px;width:900px;height:303px;background:var(--panel)}
.how h2{position:absolute;top:42px}
.step{position:absolute;top:86px;width:130px;margin-left:-65px;text-align:center}
.step-badge{position:relative;height:84px}
.step-num{position:absolute;left:18px;top:12px;font-family:'Rajdhani',sans-serif;font-size:58px;line-height:58px;font-weight:400;color:var(--ink)}
.step-ring{position:absolute;left:42px;top:4px;width:80px;height:80px;border:1px solid #d3d3d3;border-radius:50%}
.step-icon{position:absolute;left:56px;top:29px}
.step h4{font-size:7.5px;font-weight:700;letter-spacing:.8px;margin-top:14px}
.step p{font-size:6.5px;line-height:10px;color:var(--muted);margin-top:12px;padding:0 12px}
.red-rule{background:var(--red);height:2px}

/* cta */
.cta-btns{top:2793px;left:0;width:900px;display:flex;justify-content:center;gap:12px}
.cta-btns .btn{height:22px;line-height:22px;width:96px}
.btn-call{background:#3b3b3b}

.video{left:0;top:2862px;width:900px;height:281px;background:
  radial-gradient(ellipse 18% 20% at 58% 62%,rgba(245,245,245,.75),transparent 70%),
  linear-gradient(180deg,#6e7a68,#a09583 35%,#2f8aa3 65%,#1c6b86)}
.play{position:absolute;left:425px;top:118px}

/* ebook */
.ebook-cover{left:149px;top:3191px;width:190px;height:292px;background:linear-gradient(90deg,rgba(0,0,0,.35) 0,rgba(0,0,0,0) 10%),linear-gradient(180deg,#7d8ea0,#b9c3cc 45%,#6b7d8c)}
.ebook-text{left:386px;top:3248px;width:380px}
.ebook-text h2{font-size:25px;font-weight:400;margin-bottom:28px}
.ebook-text p{font-size:10.5px;line-height:16px;color:#555;margin-bottom:16px}
.ebook-text .btn{width:98px;height:20px;line-height:20px;margin-top:6px}

/* footer */
.footer{left:0;top:3533px;width:900px;height:287px;background:var(--footer);color:#d8d8d8}
.f-col{position:absolute;top:46px;font-size:6.8px;line-height:17px}
.f-col h5{font-size:8px;font-weight:600;letter-spacing:.6px;color:#fff;margin-bottom:6px}
.f-contact .phone{color:var(--red);font-size:9px}
.f-contact .mail{color:var(--red)}
.socials{display:flex;gap:6px;margin-top:10px}
.socials span{width:20px;height:20px;border-radius:50%;background:#777}
.socials span.on{background:var(--red)}
.f-bottom{position:absolute;top:226px;font-size:6.5px;color:#bbb}
.f-legal{left:378px;display:flex;gap:20px}
.badge{position:absolute;top:214px}
</style>
</head>
<body>
<div class="site">

  <header>
    <div class="abs brand"><span class="brand-mark"></span><span class="brand-name">MERIDIAN<small>SAILING</small></span></div>
    <nav class="abs top-links"><span>Blog</span><span>Gallery</span><span>About Us</span><span>Contact Us</span></nav>
    <span class="abs btn btn-header">Email Now</span>
    <nav class="abs main-nav"><span>Destinations</span><span>Liveboard Courses</span><span>Our Tribe</span><span>Online Masterclasses</span></nav>
  </header>

  <section class="photo hero" role="img" aria-label="Yacht deck with a set dining table overlooking the open sea">
    <h1 class="display">Embark on a lifetime of adventures</h1>
    <span class="btn btn-dark">Email Now</span>
    <div class="learn">LEARN TO SAIL IN A WEEK</div>
  </section>

  <section class="photo stakes" role="img" aria-label="Sailboats under warm sunset light on calm water">
    <h2 class="display">The stakes are high...</h2>
    <p>Sailing can be <b>daunting, expensive,<br>overwhelming...</b></p>
  </section>

  <h2 class="abs display section-title" style="top:890px">Embark successfully</h2>
  <div class="abs card card-1" role="img" aria-label="Friends smiling aboard a sailboat">Gain the skills, experience and formal certifications to successfully embark on your sailing journey</div>
  <div class="abs card card-2" role="img" aria-label="Couple relaxing on a sailboat at sea">You deserve an incredible adventure, award-winning instructors, sexy new sailboats and a fun learning environment</div>
  <div class="abs card card-3" role="img" aria-label="Rocky island coast with turquoise water">Enjoy sailing adventures with friends and family in exotic destinations</div>

  <h2 class="abs display section-title" style="top:1232px">The ultimate liveboards<br>sailing courses</h2>

  <div class="photo tile tile-alumni" role="img" aria-label="Sailors jumping from a yacht into the sea">
    <h3>4000+ alumni sailing<br>the world</h3>
    <p>Here at Meridian, we help thousands of people turn their sailing dreams into a reality</p>
  </div>
  <div class="photo tile tile-instructors" role="img" aria-label="Sailboat heeling on a stormy evening sea">
    <h3>Outstanding instructors</h3>
    <p>Award-winning instructor, educators first and foremost, not just great sailors!</p>
  </div>
  <div class="photo tile tile-reviews" role="img" aria-label="Aerial view of a boat in a green tropical bay">
    <h3>Outstanding reviews</h3>
    <p>We are the highest-rated ISB Sailing School, check out some of the reviews in SeaRate.</p>
    <div class="review-icons"><span></span><span></span></div>
  </div>
  <div class="photo tile tile-certified" role="img" aria-label="Aerial view of islands and moored boats">
    <h3>Official ISB certified facility</h3>
    <p>We are officially certified to supply international sailing board training for sailors looking for open water skipper badges.</p>
  </div>
  <div class="photo tile tile-charter" role="img" aria-label="Sailor at the helm of a yacht">
    <h3>Official sailing school for<br>blue horizon charter</h3>
    <p>We are the official sailing school for Blue Horizon Charter, the largest charter company in the world.</p>
  </div>

  <h2 class="abs display section-title" style="top:2235px">As featured in</h2>
  <div class="abs press"><span>Open Water</span><span>Hull &amp; Sail</span><span>Fortune Line</span><span>Voyage Weekly</span><span>Coastal Post</span></div>

  <section class="abs how">
    <h2 class="display section-title">How it works</h2>
    <div class="step" style="left:216px">
      <div class="step-badge"><span class="step-ring"></span><span class="step-num">1</span>
        <svg class="step-icon" width="26" height="26" viewBox="0 0 26 26" fill="none" stroke="#e8351f" stroke-width="2"><path d="M5 16v-3a8 8 0 0 1 16 0v3"/><rect x="3" y="15" width="5" height="7" rx="1"/><rect x="18" y="15" width="5" height="7" rx="1"/></svg></div>
      <h4>CONNECT WITH US</h4><p>What are your sailing goals and dreams? Sailing and boating experience?</p>
    </div>
    <div class="step" style="left:372px">
      <div class="step-badge"><span class="step-ring"></span><span class="step-num">2</span>
        <svg class="step-icon" width="26" height="26" viewBox="0 0 26 26" fill="none" stroke="#e8351f" stroke-width="2"><rect x="5" y="4" width="16" height="19" rx="1"/><path d="M9 10h8M9 14h8M9 18h6"/></svg></div>
      <h4>PLAN YOUR TRIP</h4><p>We work on a curated trip for you, confirming destination, vessel, timing and instructor</p>
    </div>
    <div class="step" style="left:525px">
      <div class="step-badge"><span class="step-ring"></span><span class="step-num">3</span>
        <svg class="step-icon" width="26" height="26" viewBox="0 0 26 26" fill="none" stroke="#e8351f" stroke-width="2"><rect x="3" y="11" width="5" height="11"/><path d="M8 12l5-8c2 0 3 1 2 5h6c1 0 2 1 2 2l-2 9c0 1-1 2-2 2H8"/></svg></div>
      <h4>PREPARE</h4><p>We send you resources to help you start planning, studying and preparing for your trip</p>
    </div>
    <div class="step" style="left:680px">
      <div class="step-badge"><span class="step-ring"></span><span class="step-num">4</span>
        <svg class="step-icon" width="26" height="26" viewBox="0 0 26 26" fill="none" stroke="#e8351f" stroke-width="2"><circle cx="13" cy="10" r="6"/><path d="M9 15l-3 8 4-2 2 3 1-6M17 15l3 8-4-2-2 3"/></svg></div>
      <h4>EMBARK</h4><p>Sail on the trip of a lifetime...</p>
    </div>
  </section>
  <div class="abs red-rule" style="left:149px;top:2703px;width:601px"></div>

  <h2 class="abs display section-title" style="top:2742px">Start your sailing journey now</h2>
  <div class="abs cta-btns"><span class="btn btn-call">Call 800-555-0142</span><span class="btn">Email Now</span></div>

  <div class="abs red-rule" style="left:149px;top:2860px;width:601px"></div>
  <section class="photo video" role="img" aria-label="Motor yacht cruising past rocky cliffs in turquoise water">
    <svg class="play" width="48" height="48" viewBox="0 0 48 48" fill="none" stroke="#fff" stroke-width="2.5"><circle cx="24" cy="24" r="21"/><path d="M19 15l14 9-14 9z"/></svg>
  </section>

  <div class="abs ebook-cover" role="img" aria-label="E-book cover with a rowing boat on a misty shore"></div>
  <div class="abs ebook-text">
    <h2 class="display">Receive your free e-book</h2>
    <p>We've run so many courses, we know exactly what is needed to turn your from a sailor into a skipper.</p>
    <p>Here are our 5 top tips to help you successfully embark on your sailing journey.</p>
    <span class="btn">Download the PDF</span>
  </div>

  <footer class="abs footer">
    <div class="f-col f-contact" style="left:149px">
      <h5>CONTACT US</h5>
      <div class="phone">800-555-0142</div>
      <div class="mail">Email us</div>
      <div style="line-height:10px">Meridian Sailing, PO Box 1200,<br>Harbor Point, Colorado,<br>80000</div>
      <div class="socials"><span></span><span class="on"></span><span></span></div>
    </div>
    <div class="f-col" style="left:304px">
      <h5>DESTINATIONS</h5>
      <div>Sea of Cortez, Mexico</div><div>Grenadines, Caribbean</div><div>Bahamas, Caribbean</div><div>Tahiti, South Pacific</div><div>Mallorca, Spain</div><div>Tonga Cruises</div><div>Bespoke Trips</div>
    </div>
    <div class="f-col" style="left:459px">
      <h5>DISCOVER</h5>
      <div>Liveboard Courses</div><div>Our Tribe</div><div>Online Masterclasses</div><div>Instructors</div><div>Boats</div>
    </div>
    <div class="f-col" style="left:614px">
      <h5>EXPLORE</h5>
      <div>Blog</div><div>Gallery</div><div>About Us</div><div>Contact Us</div>
    </div>
    <div class="f-bottom" style="left:149px">© 2020 Meridian Sailing. All Rights Reserved</div>
    <div class="f-bottom f-legal"><span>Sitemap</span><span>Privacy Policy</span><span>Terms of Use</span></div>
    <span class="badge" style="left:614px;top:218px;width:46px;height:26px;background:#e9e9e9"></span>
    <span class="badge" style="left:676px;width:48px;height:48px;border-radius:50%;background:#2f5fa8"></span>
    <svg class="badge" style="left:820px;top:224px" width="14" height="14" viewBox="0 0 14 14"><path d="M7 2l5 10H2z" fill="#e8351f"/></svg>
  </footer>

</div>
</body>
</html>
```